Veterinary Clinic Letterhead - Ridgeview Veterinary Surgery

We need a letterhead design for an established Veterinary Clinic in Mareeba called Ridgeview Veterinary Surgery. We are a moderate sized mixed animal veterinary clinic offering a wide variety of veterinary services. The design should use the same colour pattern as those in the logos supplied. The design should also include our address (48 Tulloch Road, Tarrin Creek, Northvale, 4872), phone number (07 4158 6734), email (admin@ridgeviewvets.com.au), website (www.ridgeviewvets.com.au) and our opening hours (7:30am to 5:30pm Monday to Friday and 8am to 1pm Saturday).
Target Market(s)
Pet owners
Industry/Entity Type
Veterinary
Requirements
Must have
- The logo or modification of it, business address, opening hours, website, phone number and email address

```html
<!DOCTYPE html>
<html lang="en">
<head>
<meta charset="utf-8">
<title>Ridgeview Veterinary Surgery – Stationery</title>
<link rel="stylesheet" href="https://fonts.googleapis.com/css2?family=Montserrat:wght@600&family=Open+Sans:wght@400&family=Roboto:wght@400&display=swap">
<style>
  :root {
    --navy: #0e2a4c;
    --paper: #f6f6f3;
    --ink: #3a3a3a;
    --backdrop: #dcddd9;
    --white: #ffffff;
  }
  * { box-sizing: border-box; margin: 0; padding: 0; }
  html, body { width: 1200px; height: 1115px; overflow: hidden; }
  body {
    background: var(--backdrop);
    font-family: "Open Sans", sans-serif;
    position: relative;
  }
  .letterhead {
    position: absolute;
    left: 60px; top: 57px;
    width: 707px; height: 1000px;
    background: var(--paper);
    box-shadow: 0 10px 30px rgba(0,0,0,0.12);
    padding: 52px 86px 40px;
    display: flex; flex-direction: column;
  }
  .brand {
    display: flex; flex-direction: column; align-items: center;
    color: var(--navy);
  }
  .brand-dot {
    width: 62px; height: 62px; border-radius: 50%;
    background: var(--navy);
    margin-bottom: 8px;
  }
  .brand-name {
    font-family: "Montserrat", sans-serif;
    font-weight: 600;
    font-size: 15px;
    letter-spacing: 0.08em;
    text-transform: uppercase;
    text-align: center;
  }
  .brand-rule {
    width: 230px; height: 1px; background: currentColor; margin-top: 5px;
  }
  .hours {
    text-align: center;
    font-size: 13px;
    color: var(--ink);
    margin-top: 14px;
  }
  .letter-body {
    margin-top: 70px;
    font-size: 12.5px;
    line-height: 1.55;
    color: var(--ink);
  }
  .letter-body p { margin-bottom: 22px; }
  .letter-body .closing { margin-bottom: 0; }
  .signature {
    width: 90px; height: 70px; margin-top: 10px;
    background: linear-gradient(135deg, #e9e9e6, #dcdcd8);
  }
  .contact {
    margin-top: auto;
    text-align: center;
    font-family: "Roboto", sans-serif;
    font-size: 13px;
    color: var(--ink);
    line-height: 1.7;
  }
  .contact-line { display: flex; justify-content: center; align-items: center; gap: 6px; }
  .contact-line svg { width: 12px; height: 12px; fill: var(--navy); flex: none; }
  .card {
    position: absolute;
    left: 805px;
    width: 360px; height: 206px;
    box-shadow: 0 8px 24px rgba(0,0,0,0.14);
    display: flex; align-items: center; justify-content: center;
  }
  .card-light { top: 150px; background: var(--paper); color: var(--navy); }
  .card-dark { top: 420px; background: var(--navy); color: var(--white); }
  .card .brand { color: inherit; }
  .card-dark .brand-dot { background: var(--white); }
  .card .brand-name { font-size: 14px; }
  .card .brand-rule { width: 210px; }
</style>
</head>
<body>
  <article class="letterhead">
    <header class="brand">
      <div class="brand-dot"></div>
      <div class="brand-name">Ridgeview Veterinary Surgery</div>
      <div class="brand-rule"></div>
    </header>
    <p class="hours">7:30am to 5:30pm Monday to Friday and 8am to 1pm Saturday</p>

    <section class="letter-body">
      <p>Dear customer,</p>
      <p>Lorem ipsum dolor sit amet, consectetur adipisicing elit, sed do eiusmod tempor incididunt ut labore et dolore magna aliqua. Ut enim ad minim veniam, quis nostrud exercitation ullamco laboris nisi ut aliquip ex ea commodo consequat. Duis aute irure dolor in reprehenderit in voluptate velit esse cillum dolore eu fugiat nulla pariatur. Excepteur sint occaecat cupidatat non proident, sunt in culpa qui officia deserunt mollit anim id est laborum.</p>
      <p>Lorem ipsum dolor sit amet, consectetur adipisicing elit, sed do eiusmod tempor incididunt ut labore et dolore magna aliqua. Ut enim ad minim veniam, quis nostrud exercitation ullamco laboris nisi ut aliquip ex ea commodo consequat. Duis aute irure dolor in reprehenderit in voluptate velit esse cillum dolore eu fugiat nulla pariatur. Excepteur sint occaecat cupidatat non proident, sunt in culpa qui officia deserunt mollit anim id est laborum.</p>
      <p>Lorem ipsum dolor sit amet, consectetur adipisicing elit, sed do eiusmod tempor incididunt ut labore et dolore magna aliqua. Ut enim ad minim veniam, quis nostrud exercitation ullamco laboris nisi ut aliquip ex ea commodo consequat. Duis aute irure dolor in reprehenderit in voluptate velit esse cillum dolore eu fugiat nulla pariatur. Excepteur sint occaecat cupidatat non proident, sunt in culpa qui officia deserunt mollit anim id est laborum.</p>
      <p>Lorem ipsum dolor sit amet, consectetur adipisicing elit, sed do eiusmod tempor incididunt ut labore et dolore magna aliqua. Ut enim ad minim veniam, quis nostrud exercitation ullamco laboris nisi ut aliquip ex ea commodo consequat. Duis aute irure dolor in reprehenderit.</p>
      <p class="closing">Yours Sincerely,</p>
      <div class="signature" role="img" aria-label="Handwritten signature of the sender"></div>
    </section>

    <footer class="contact">
      <div>48 Tulloch Road, Tarrin Creek, Northvale, 4872</div>
      <div class="contact-line">
        <svg viewBox="0 0 24 24" aria-hidden="true"><path d="M6.6 10.8a15.1 15.1 0 0 0 6.6 6.6l2.2-2.2c.3-.3.7-.4 1-.2 1.1.4 2.3.6 3.6.6.6 0 1 .4 1 1V20c0 .6-.4 1-1 1A17 17 0 0 1 3 4c0-.6.4-1 1-1h3.5c.6 0 1 .4 1 1 0 1.3.2 2.5.6 3.6.1.3 0 .7-.2 1z"/></svg>
        <span>07 4158 6734</span>
        <svg viewBox="0 0 24 24" aria-hidden="true"><path d="M2 5h20v14H2zm2 2v.5l8 5 8-5V7zm0 3v7h16v-7l-8 5z"/></svg>
        <span>admin@ridgeviewvets.com.au</span>
        <svg viewBox="0 0 24 24" aria-hidden="true"><path d="M12 2a10 10 0 1 0 0 20 10 10 0 0 0 0-20zm6.9 6h-3a15 15 0 0 0-1.3-3.9A8 8 0 0 1 18.9 8zM12 4c.8 1.2 1.5 2.5 1.9 4h-3.8c.4-1.5 1.1-2.8 1.9-4zM4.3 14a8 8 0 0 1 0-4h3.4a16 16 0 0 0 0 4zm.8 2h3a15 15 0 0 0 1.3 3.9A8 8 0 0 1 5.1 16zm3-8h-3a8 8 0 0 1 4.3-3.9A15 15 0 0 0 8.1 8zM12 20c-.8-1.2-1.5-2.5-1.9-4h3.8c-.4 1.5-1.1 2.8-1.9 4zm2.3-6H9.7a14 14 0 0 1 0-4h4.6a14 14 0 0 1 0 4zm.3 5.9a15 15 0 0 0 1.3-3.9h3a8 8 0 0 1-4.3 3.9zm1.7-5.9a16 16 0 0 0 0-4h3.4a8 8 0 0 1 0 4z"/></svg>
        <span>www.ridgeviewvets.com.au</span>
      </div>
    </footer>
  </article>

  <section class="card card-light">
    <div class="brand">
      <div class="brand-dot"></div>
      <div class="brand-name">Ridgeview Veterinary Surgery</div>
      <div class="brand-rule"></div>
    </div>
  </section>

  <section class="card card-dark">
    <div class="brand">
      <div class="brand-dot"></div>
      <div class="brand-name">Ridgeview Veterinary Surgery</div>
      <div class="brand-rule"></div>
    </div>
  </section>
</body>
</html>
```